The Brindlewick Project

All information regarding the design is located at Brindlewick.com. Any questions regarding the project, will be answered on the site.

```html
<!DOCTYPE html>
<html lang="en">
<head>
<meta charset="utf-8">
<title>Brindlewick</title>
<link href="https://fonts.googleapis.com/css2?family=PT+Sans:wght@400;700&display=swap" rel="stylesheet">
<style>
  :root {
    --bar-bg: #01131b;
    --bar-text: #ffffff;
    --header-tint: #f2f7fa;
    --page-bg: #ffffff;
    --brand: #5b93a8;
    --field-border: #c6d6dd;
    --placeholder: #9a9a9a;
    --go-text: #1c4e64;
    --go-top: #ffffff;
    --go-bottom: #e3f1f8;
    --login-text: #7a7a7a;
    --login-border: #cfcfcf;
    --footer-bg: #f9f9f9;
    --footer-line: #eeeeee;
    --footer-text: #ababab;
  }
  * { box-sizing: border-box; margin: 0; padding: 0; }
  html, body {
    width: 1200px; height: 706px; overflow: hidden;
    background: var(--page-bg);
    font-family: "PT Sans", Tahoma, sans-serif;
  }
  .canvas { position: relative; width: 1200px; height: 706px; }

  .top-nav {
    position: absolute; top: 0; left: 0; width: 100%; height: 30px;
    background: var(--bar-bg);
  }
  .top-nav a {
    position: absolute; top: 8px;
    color: var(--bar-text); text-decoration: none;
    font-size: 12px; letter-spacing: 0.2px; line-height: 14px;
  }

  .header-band {
    position: absolute; top: 30px; left: 0; width: 100%; height: 75px;
    background: linear-gradient(to bottom, var(--header-tint), var(--page-bg));
  }
  .login-button {
    position: absolute; top: 43px; left: 1088px; width: 98px; height: 31px;
    border: 1px solid var(--login-border); border-radius: 2px;
    background: linear-gradient(to bottom, #fafafa, #e8e8e8);
    color: var(--login-text); font-size: 15px; line-height: 29px;
    text-align: center; letter-spacing: 0.5px;
  }

  .brand {
    position: absolute; top: 252px; left: 0; width: 1200px;
    display: flex; justify-content: center; align-items: center; gap: 14px;
  }
  .brand-dot {
    width: 18px; height: 18px; border-radius: 50%; background: var(--brand);
  }
  .brand-name {
    color: var(--brand); font-size: 54px; font-weight: 400; line-height: 64px;
  }

  .search {
    position: absolute; top: 333px; left: 304px;
    display: flex; gap: 7px;
  }
  .search-field {
    width: 525px; height: 36px;
    border: 1px solid var(--field-border);
    background: linear-gradient(to bottom, #f4f6f7, #ffffff 40%);
    color: var(--placeholder); font-size: 14px; line-height: 34px;
    padding-left: 14px;
  }
  .search-go {
    width: 60px; height: 36px;
    border: 1px solid var(--field-border);
    background: linear-gradient(to bottom, var(--go-top), var(--go-bottom));
    color: var(--go-text); font-size: 17px; line-height: 34px;
    text-align: center; letter-spacing: 0.5px;
  }

  .site-footer {
    position: absolute; top: 660px; left: 0; width: 100%; height: 46px;
    background: var(--footer-bg); border-top: 1px solid var(--footer-line);
    color: var(--footer-text); font-size: 11px;
  }
  .site-footer span { position: absolute; top: 18px; line-height: 14px; }
</style>
</head>
<body>
<div class="canvas">
  <nav class="top-nav">
    <a style="left:14px">WEB</a>
    <a style="left:71px">IMAGES</a>
    <a style="left:145px">VIDEOS</a>
    <a style="left:217px">NEWS</a>
    <a style="left:281px">MAPS</a>
  </nav>

  <div class="header-band"></div>
  <div class="login-button">LOGIN</div>

  <div class="brand">
    <span class="brand-dot"></span>
    <span class="brand-name">Brindlewick</span>
  </div>

  <div class="search">
    <div class="search-field">Ask your question here</div>
    <div class="search-go">GO</div>
  </div>

  <footer class="site-footer">
    <span style="left:15px">Copyright © 2013 Brindlewick. All rights reserved</span>
    <span style="left:920px">Privacy Policy</span>
    <span style="left:1005px">|</span>
    <span style="left:1026px">Terms of use</span>
  </footer>
</div>
</body>
</html>
```